K7R Business Cards

Business Cards

Contact Information for Business Card

Company name, owner name, license #s, phone & email

Requirements
Should not have
• mailing address

```html
<!DOCTYPE html>
<html lang="en">
<head>
<meta charset="utf-8">
<title>K7R Business Cards</title>
<link rel="stylesheet" href="https://fonts.googleapis.com/css2?family=Poppins:wght@400;500;700;800&display=swap">
<style>
  :root {
    --stage: #2d2d2d;
    --card: #000000;
    --brand-blue: #0a3aa8;
    --accent-red: #d0141a;
    --ink: #ffffff;
    --photo-dark: #0a0a0a;
    --photo-mid: #2b2b2e;
  }
  * { box-sizing: border-box; margin: 0; padding: 0; }
  html, body { width: 1200px; height: 1015px; overflow: hidden; }
  body {
    background: var(--stage);
    font-family: "Poppins", sans-serif;
    position: relative;
  }
  .business-card {
    position: absolute;
    width: 760px;
    height: 434px;
    background: var(--card);
    overflow: hidden;
    box-shadow: 0 12px 30px rgba(0,0,0,.55);
  }
  .business-card--realty { left: 110px; top: 50px; }
  .business-card--construction { left: 330px; top: 530px; }

  .portrait {
    position: absolute;
    right: 0; top: 0;
    width: 300px; height: 420px;
    background: radial-gradient(ellipse 60% 70% at 60% 65%, var(--photo-mid) 0%, #1a1a1c 55%, var(--photo-dark) 100%);
  }
  .base-band {
    position: absolute;
    left: 0; right: 0; bottom: 0;
    height: 14px;
    background: var(--brand-blue);
  }

  .card-content {
    position: absolute;
    left: 70px; top: 80px;
    width: 370px;
  }
  .brand {
    display: flex; align-items: center; gap: 12px;
  }
  .brand-mark {
    width: 18px; height: 18px; border-radius: 50%;
    background: var(--brand-blue);
  }
  .brand-name {
    font-weight: 800;
    font-size: 64px;
    line-height: 1;
    color: var(--brand-blue);
    letter-spacing: 2px;
  }
  .brand-division {
    margin: 4px 0 0 100px;
    font-weight: 700;
    font-size: 30px;
    color: var(--ink);
    line-height: 1.1;
  }
  .business-card--construction .brand-division {
    margin-left: 30px;
    font-size: 30px;
    letter-spacing: 1px;
  }
  .owner-name {
    margin-top: 26px;
    font-weight: 800;
    font-size: 30px;
    color: var(--brand-blue);
    text-transform: uppercase;
    letter-spacing: .5px;
    line-height: 1.1;
  }
  .rule {
    width: 90px; height: 2px;
    background: var(--accent-red);
    margin: 10px 0 8px 30px;
  }
  .contact-list { list-style: none; margin-left: 30px; }
  .contact-list li {
    display: flex; align-items: center; gap: 12px;
    color: var(--ink);
    font-size: 19px;
    line-height: 1.4;
    white-space: nowrap;
  }
  .contact-list svg { width: 18px; height: 18px; flex: none; }
  .licenses {
    list-style: none;
    margin-left: 60px;
    color: var(--ink);
    font-size: 19px;
    line-height: 1.4;
    white-space: nowrap;
  }
</style>
</head>
<body>

<section class="business-card business-card--realty">
  <div class="portrait" role="img" aria-label="Studio portrait of the agent in a dark suit, white shirt and patterned tie"></div>
  <div class="card-content">
    <div class="brand">
      <span class="brand-mark"></span>
      <span class="brand-name">K7R</span>
    </div>
    <p class="brand-division">Realty</p>
    <h2 class="owner-name">Dale Marwick</h2>
    <div class="rule"></div>
    <ul class="contact-list">
      <li>
        <svg viewBox="0 0 24 24" fill="var(--brand-blue)"><path d="M6.6 10.8a15 15 0 0 0 6.6 6.6l2.2-2.2a1 1 0 0 1 1-.25 11.4 11.4 0 0 0 3.6.57 1 1 0 0 1 1 1V20a1 1 0 0 1-1 1A17 17 0 0 1 3 4a1 1 0 0 1 1-1h3.5a1 1 0 0 1 1 1c0 1.25.2 2.45.57 3.57a1 1 0 0 1-.25 1z"/></svg>
        555-014-2290
      </li>
      <li>
        <svg viewBox="0 0 24 24" fill="var(--brand-blue)"><path d="M2 5h20v14H2z M2 5l10 8 10-8" stroke="#000" stroke-width="1.4"/></svg>
        jdalemarwick@inboxmail.com
      </li>
    </ul>
    <div class="rule"></div>
    <ul class="licenses">
      <li>Real Estate Lic. #RE-4071582</li>
      <li>Broker Lic. #BR-2093318</li>
    </ul>
  </div>
  <div class="base-band"></div>
</section>

<section class="business-card business-card--construction">
  <div class="portrait" role="img" aria-label="Studio portrait of the contractor in a dark suit, white shirt and patterned tie"></div>
  <div class="card-content">
    <div class="brand">
      <span class="brand-mark"></span>
      <span class="brand-name">K7R</span>
    </div>
    <p class="brand-division">CONSTRUCTION</p>
    <h2 class="owner-name">Dale Marwick</h2>
    <div class="rule"></div>
    <ul class="contact-list">
      <li>
        <svg viewBox="0 0 24 24" fill="var(--brand-blue)"><path d="M6.6 10.8a15 15 0 0 0 6.6 6.6l2.2-2.2a1 1 0 0 1 1-.25 11.4 11.4 0 0 0 3.6.57 1 1 0 0 1 1 1V20a1 1 0 0 1-1 1A17 17 0 0 1 3 4a1 1 0 0 1 1-1h3.5a1 1 0 0 1 1 1c0 1.25.2 2.45.57 3.57a1 1 0 0 1-.25 1z"/></svg>
        555-014-2290
      </li>
      <li>
        <svg viewBox="0 0 24 24" fill="var(--brand-blue)"><path d="M2 5h20v14H2z M2 5l10 8 10-8" stroke="#000" stroke-width="1.4"/></svg>
        jdalemarwick@inboxmail.com
      </li>
    </ul>
    <div class="rule"></div>
    <ul class="licenses">
      <li>Contractor Lic. #BC-7731046</li>
      <li>Builder Lic. #RB-5582907</li>
    </ul>
  </div>
  <div class="base-band"></div>
</section>

</body>
</html>
```